Twelve Lanterns Along Harbourside Tour Flyer

I need a one page flyer, one sided, full color. The main part of the flyer should be ONLY ONE of the attached photos. All text is included with SAMPLE/EXAMPLE sizing, but actual sizing and placement, and FONT are up to you. Font should be clear and legible, and one font should be used for all titles/larger text, and another for all small/paragraph text.

Tour

```html
<!DOCTYPE html>
<html lang="en">
<head>
<meta charset="utf-8">
<title>Twelve Lanterns Along Harbourside Tour Flyer</title>
<link rel="stylesheet" href="https://fonts.googleapis.com/css2?family=Tinos:ital,wght@0,400;0,700;1,400;1,700&display=swap">
<style>
  :root {
    --page: #1c1c1c;
    --panel-top: #2a2a2a;
    --panel-bottom: #151515;
    --copper: #9c4f22;
    --gold: #e6b85a;
    --text: #f2f2f2;
    --muted: #9a9a9a;
    --rule: #8a8a8a;
    --photo-light: #4a4442;
    --photo-dark: #181818;
  }
  * { margin: 0; padding: 0; box-sizing: border-box; }
  html, body { width: 1000px; height: 1200px; overflow: hidden; background: var(--page); }
  .flyer {
    position: relative; width: 1000px; height: 1200px;
    background: radial-gradient(ellipse at 60% 35%, var(--panel-top), var(--panel-bottom) 75%);
    font-family: "Tinos", "Times New Roman", serif;
    color: var(--text);
  }
  .frame {
    position: absolute; left: 44px; top: 44px; width: 912px; height: 1114px;
    border: 6px solid transparent;
    border-image: linear-gradient(135deg, var(--copper), var(--gold) 45%, var(--copper) 70%, var(--gold)) 1;
  }
  .gold-text {
    background: linear-gradient(90deg, var(--copper), var(--gold) 45%, var(--copper));
    -webkit-background-clip: text; background-clip: text; color: transparent;
  }
  .title {
    position: absolute; left: 0; right: 0; top: 82px; text-align: center;
    font-size: 45px; font-weight: 700; z-index: 2;
  }
  .subtitle {
    position: absolute; left: 130px; top: 142px; font-size: 23px; font-style: italic;
    font-weight: 700; color: var(--muted); z-index: 2;
  }
  .hero-photo {
    position: absolute; left: 340px; top: 92px; width: 580px; height: 700px;
    background: radial-gradient(ellipse at 50% 40%, var(--photo-light), var(--photo-dark) 70%, transparent 90%);
  }
  .inset-photo {
    position: absolute; left: 62px; top: 778px; width: 270px; height: 372px;
    background: radial-gradient(ellipse at 50% 45%, var(--photo-light), var(--photo-dark) 75%);
  }
  .intro, .details, .bio { position: absolute; font-size: 20px; line-height: 29px; z-index: 2; text-align: justify; hyphens: auto; }
  .intro { left: 84px; top: 232px; width: 372px; }
  .intro strong { font-size: 21px; }
  .details { left: 84px; top: 410px; width: 262px; line-height: 28.5px; }
  .details .name { font-weight: 700; font-size: 21px; letter-spacing: 1px; }
  .press { position: absolute; right: 83px; text-align: right; font-size: 21px; line-height: 26px; z-index: 2; }
  .press .source { color: var(--muted); font-size: 19px; }
  .press .source.bold { font-weight: 700; font-size: 20px; }
  .press-one { top: 598px; }
  .press-rule { position: absolute; left: 509px; top: 666px; width: 408px; height: 1px; background: var(--rule); z-index: 2; }
  .press-two { top: 680px; }
  .bio { left: 352px; top: 792px; width: 565px; font-size: 20px; line-height: 28.4px; }
  .tagline { position: absolute; left: 352px; top: 1040px; font-size: 26px; font-weight: 700; line-height: 36px; z-index: 2; }
</style>
</head>
<body>
<div class="flyer">
  <div class="hero-photo" role="img" aria-label="Portrait photo of the singer in a dark suit and tie holding a studio microphone"></div>
  <div class="inset-photo" role="img" aria-label="Smaller photo of the singer in a dark jacket holding his lapels"></div>
  <div class="frame"></div>

  <h1 class="title gold-text">“Twelve Lanterns Along Harbourside”</h1>
  <p class="subtitle">with the Rowan Ashby Trio</p>

  <p class="intro">The world’s most beloved melodies in ten languages featuring songs like <strong>“Willow Glen”</strong>, <strong>“Le Ciel d’Argent”</strong>, <strong>“Canta Mañana”</strong>, <strong>“Lantern On The Quiet Harbour”</strong>, and more!</p>

  <p class="details">Original, arrangements by an <em>Lumen-winning composer</em> tap into the rare talent of countertenor, <span class="name">Rowan Ashby</span>, and his soloist collaborators, an outstanding Ellsworth-trained concert pianist, and a wind soloist from the Eastport Philharmonic on oboe, english horn, flute, and clarinet.</p>

  <div class="press press-one">
    <p>“Ashby has Star Quality”</p>
    <p class="source">Riverton Daily Ledger</p>
  </div>
  <div class="press-rule"></div>
  <div class="press press-two">
    <p>“Performances of Great Vitality and Verve”</p>
    <p class="source bold">Westbay Evening Post</p>
  </div>

  <p class="bio">Rowan Ashby has performed around the world from Marlowe Concert Hall, to Korvin Hall using extraordinary vocal range, versatility, and a hilarious rapport with the audience, to entertain. A full time member of the Aurelia-winning ensemble Halcyon Voices, his voice can be heard on every major record label with a range of artists from Celia Marsh to the Northgate Philharmonic.</p>

  <p class="tagline gold-text">The World’s Favorite Melodies<br>Like You’ve Never Heard Them Before!</p>
</div>
</body>
</html>
```